Powerpoint Design and Build

We need to create PowerPoint for program called Glimmerly Orbit. Glimmerly Orbit is an online system that helps association volunteers track their volunteer hours and the impact that are having with engineering outreach initiatives.

We have an established logo for the brand, which you will find under Files.

The following colors are used in the brand:

Blue/green: PMS 3262 C

Purple: PMS 525 C

Lime: PMS 381 C

Grey: PMS Cool Grey 11

Headline and body fonts should be restricted to a common sans serif such as arial or helvetica

For reference, The tagline "Every Hour Shines Bright" is set in Gotham Book; match to this.

The identity needs to be locked up with the Coalition of Harbor Artisans logo in grey, which you'll find attached. See the file "Glimmerly_orbit_lock-up.psd" for reference, but please recreate as a vector element.

As an idea of Powerpoint created for a different Coalition of Harbor Artisans program, place see the Tessera Powerpoint. FOR Reference only

NOTE: please maximize the area for content and stick to a white background.

Final deliverables are:

Design for presentation title slide, section title slide and content slide, including styles for headlines, subheads, bullet points and straight copy. Also include slide numbers in footer.

To repeat, we expect separate art elements created in Illustrator, and a completed Powerpoint template with master slides.

Professional and Collegiate Women in Engineering

Engineering

• Design for presentation title slide, section title slide and content slide, including styles for headlines, subheads, bullet points and straight copy. Also include slide numbers in footer.

```html
<!DOCTYPE html>
<html lang="en">
<head>
<meta charset="utf-8">
<title>Glimmerly Orbit – Presentation Template</title>
<link rel="stylesheet" href="https://fonts.googleapis.com/css2?family=PT+Sans:wght@400;700&family=Open+Sans:wght@800&display=swap">
<style>
  :root{
    --backdrop:#4a2b1f;
    --white:#ffffff;
    --purple:#512d6d;
    --teal:#1aa8a5;
    --teal-light:#e6f4f3;
    --grey:#53565a;
    --grey-band:#6d6e71;
    --text:#4a4a4a;
    --rule:#c9c3d3;
  }
  *{box-sizing:border-box;margin:0;padding:0}
  html,body{width:1200px;height:646px;overflow:hidden}
  body{background:var(--backdrop);font-family:"PT Sans",Arial,sans-serif;color:var(--text);position:relative}

  .slide{position:absolute;width:252px;height:190px;background:var(--white);overflow:hidden}
  .slide-footer{position:absolute;left:0;right:0;bottom:0;height:21px;background:var(--grey-band);
    border-top:3px solid var(--white);box-shadow:0 -2px 0 var(--purple);
    display:flex;justify-content:space-between;align-items:center;padding:0 8px 0 40px;
    font-size:5px;font-weight:700;color:var(--white)}
  .footer-mark{position:absolute;left:6px;bottom:6px;width:26px;height:26px;border-radius:50%;
    background:var(--white);border:4px solid var(--teal);z-index:2}

  .headline{position:absolute;left:26px;top:16px;font-size:11px;font-weight:700;color:var(--purple);
    letter-spacing:.2px;padding-bottom:2px;border-bottom:1px solid var(--rule)}
  .copy{font-size:5.4px;line-height:1.55;color:var(--text)}
  .justified{text-align:justify}

  .bullets{list-style:none;font-size:6px;color:var(--text)}
  .bullets li{position:relative;padding-left:10px;margin-bottom:5px}
  .bullets li::before{content:"";position:absolute;left:0;top:2px;width:3px;height:3px;background:var(--teal)}

  .lockup{position:absolute;left:0;right:0;display:flex;justify-content:center;align-items:center;gap:6px}
  .lockup-brand{display:flex;flex-direction:column}
  .lockup-name{display:flex;align-items:center;gap:3px;font-size:12px;color:var(--purple);font-weight:400}
  .lockup-dot{width:10px;height:10px;border-radius:50%;background:var(--teal)}
  .lockup-tagline{font-size:3.6px;color:var(--grey);margin-left:13px}
  .lockup-divider{width:1px;height:13px;background:var(--grey)}
  .lockup-partner{display:flex;align-items:center;gap:3px;font-size:5px;line-height:1.1;color:var(--grey);max-width:70px}
  .partner-dot{width:8px;height:8px;border-radius:50%;background:#9a9b9c;flex:none}

  .photo{position:absolute;background:linear-gradient(135deg,#d96a92 0%,#b95a78 45%,#e8d9d4 100%)}

  .data-table{position:absolute;left:40px;top:45px;width:188px;border-collapse:collapse;font-size:5px}
  .data-table th{background:var(--teal);color:var(--white);font-size:8px;height:17px;font-weight:700}
  .data-table td{height:13px;padding-left:8px;border:1px solid #cfe9e8;color:var(--text)}
  .data-table tr:nth-child(even) td{background:var(--teal-light)}

  .sub{font-size:5.2px;color:var(--text)}
  .sub-title{margin:0 0 2px 10px}
  .sub ul{list-style:none;margin-bottom:7px}
  .sub li{position:relative;padding-left:10px;line-height:1.6}
  .sub li::before{content:"";position:absolute;left:2px;top:3px;width:2px;height:2px;background:var(--text);border-radius:50%}
</style>
</head>
<body>

<!-- Title slide -->
<section class="slide" style="left:349px;top:17px">
  <div class="lockup" style="top:48px">
    <div class="lockup-brand"><div class="lockup-name"><span class="lockup-dot"></span>Glimmerly Orbit</div><div class="lockup-tagline">Every Hour Shines Bright</div></div>
    <span class="lockup-divider"></span>
    <div class="lockup-partner"><span class="partner-dot"></span>Coalition of Harbor Artisans</div>
  </div>
  <h1 style="position:absolute;top:92px;width:100%;text-align:center;font-size:13px;color:var(--purple)">TITLE OF PRESENTATION</h1>
  <p style="position:absolute;top:110px;width:100%;text-align:center;font-size:8px;color:var(--grey)">Description</p>
  <footer class="slide-footer"><span>Private/Confidential</span><span>www.GlimmerlyOrbit.com</span></footer>
</section>

<!-- Content: copy + bullets -->
<section class="slide" style="left:636px;top:17px">
  <h2 class="headline">LOREM IPSUM&nbsp; LOREM</h2>
  <p class="copy" style="position:absolute;left:42px;top:44px;width:172px">Orem ipsum dolor sit amet, consectetuer adipiscing elit, sed diam nonummy nibh euismod tincidunt ut laoreet dolore magna aliquam erat volutpat. Ut wisi enim ad minim veniam, quis nostrud exerci tation ullamcoper suscipit lobortis nisl ut aliquip ex ea commodo consequat. Duis autem vel eum iriure dolor in hendrerit in vulputate velit esse molestie</p>
  <ul class="bullets" style="position:absolute;left:42px;top:99px">
    <li>Lorem ipsum&nbsp; Lorem Lorem ipsum&nbsp; Lorem</li>
    <li>Lorem ipsum Lorem Lorem</li>
    <li>Lorem ipsum Lorem Lorem ipsum&nbsp; Lorem&nbsp; Lorem ipsum</li>
    <li>Lorem ipsum orem Lorem ipsum&nbsp; Lo</li>
    <li>Lorem ipsum Lorem</li>
  </ul>
  <span class="footer-mark"></span>
  <footer class="slide-footer"><span>Private/Confidential</span><span>www.GlimmerlyOrbit.com</span></footer>
</section>

<!-- Content: copy + photo -->
<section class="slide" style="left:923px;top:17px">
  <h2 class="headline" style="left:40px">LOREM IPSUM&nbsp; LOREM</h2>
  <p class="copy" style="position:absolute;left:40px;top:44px;width:176px">Orem ipsum dolor sit amet, consectetuer adipiscing elit, sed diam nonummy nibh euismod tincidunt ut laoreet dolore magna aliquam erat volutpat. Ut wisi enim ad minim veniam, quis nostrud exerci tation ullamcoper suscipit lobortis nisl ut aliquip ex ea commodo consequat.</p>
  <div class="photo" role="img" aria-label="Photo of volunteers in pink shirts at a hands-on activity" style="left:65px;top:84px;width:124px;height:82px"></div>
  <span class="footer-mark"></span>
  <footer class="slide-footer"><span>Private/Confidential</span><span>www.GlimmerlyOrbit.com</span></footer>
</section>

<!-- Section slide -->
<section class="slide" style="left:22px;top:219px">
  <div class="lockup" style="top:44px">
    <div class="lockup-brand"><div class="lockup-name"><span class="lockup-dot"></span>Glimmerly Orbit</div><div class="lockup-tagline">Every Hour Shines Bright</div></div>
    <span class="lockup-divider"></span>
    <div class="lockup-partner"><span class="partner-dot"></span>Coalition of Harbor Artisans</div>
  </div>
  <h1 style="position:absolute;top:82px;width:100%;text-align:center;font-size:14px;color:var(--purple)">PART 3</h1>
  <p class="copy justified" style="position:absolute;left:68px;top:110px;width:118px">Orem ipsum dolor sit amet, consectetuer adipiscing elit, sed diam nonummy nibh euismod tincidunt ut laoreet dolore magna aliquam erat volutpat. Ut wisi enim ad minim veniam, quis nostrud</p>
  <span class="footer-mark"></span>
  <footer class="slide-footer"><span>Private/Confidential</span><span>www.GlimmerlyOrbit.com</span></footer>
</section>

<!-- Content: photo + text -->
<section class="slide" style="left:349px;top:219px">
  <h2 class="headline" style="left:10px">LOREM IPSUM</h2>
  <div class="photo" role="img" aria-label="Photo of volunteers in pink shirts working together at a table" style="left:10px;top:47px;width:124px;height:96px"></div>
  <p class="copy justified" style="position:absolute;left:143px;top:46px;width:98px">Lorem ipsum dolor sit amet, consectetuer adipiscing elit, sed diam nonummy nibh euismod tincidunt ut laoreet dolore magna aliquam erat volutpat. Ut wisi enim ad minim veniam, quis nostrud exerci tation ullamcoper suscipit lobortis nisl ut aliquip ex ea commodo consequat. Duis autem vel eum iri. Lorem ipsum dolor sit amet, consectetuer adipiscing elit, sed diam nonummy nibh euismod</p>
  <span class="footer-mark"></span>
  <footer class="slide-footer"><span>Private/Confidential</span><span>www.GlimmerlyOrbit.com</span></footer>
</section>

<!-- Content: table -->
<section class="slide" style="left:636px;top:219px">
  <span style="position:absolute;right:6px;top:4px;width:34px;height:34px;border-radius:50%;border:6px solid #d8efee"></span>
  <h2 class="headline" style="left:40px">LOREM IPSUM</h2>
  <table class="data-table">
    <tr><th colspan="4">Lorem ipsum&nbsp; Lorem ipsum&nbsp; Lorem ipsum</th></tr>
    <tr><td>Lorem ipsum</td><td>Lorem ipsum</td><td>Lorem ipsum</td><td>Lorem ipsum</td></tr>
    <tr><td>Lorem ipsum</td><td>Lorem ipsum</td><td>Lorem ipsum</td><td>Lorem ipsum</td></tr>
    <tr><td>Lorem ipsum</td><td>Lorem ipsum</td><td>Lorem ipsum</td><td>Lorem ipsum</td></tr>
    <tr><td>Lorem ipsum</td><td>Lorem ipsum</td><td>Lorem ipsum</td><td>Lorem ipsum</td></tr>
    <tr><td>Lorem ipsum</td><td>Lorem ipsum</td><td>Lorem ipsum</td><td>Lorem ipsum</td></tr>
    <tr><td>Lorem ipsum</td><td>Lorem ipsum</td><td>Lorem ipsum</td><td>Lorem ipsum</td></tr>
    <tr><td>Lorem ipsum</td><td>Lorem ipsum</td><td>Lorem ipsum</td><td>Lorem ipsum</td></tr>
  </table>
  <span class="footer-mark"></span>
  <footer class="slide-footer"><span>Private/Confidential</span><span>www.GlimmerlyOrbit.com</span></footer>
</section>

<!-- Content: diagram -->
<section class="slide" style="left:923px;top:219px">
  <h2 class="headline">LOREM IPSUM</h2>
  <svg class="diagram" width="252" height="190" viewBox="0 0 252 190" style="position:absolute;left:0;top:0" font-family="PT Sans, Arial, sans-serif" font-size="4.5" fill="#fff">
    <g stroke="#8a8c8e" stroke-width="0.5" fill="none">
      <path d="M40 59 V66 H18 V112 H38"/><path d="M18 89 H40"/>
      <path d="M90 59 V70"/><path d="M76 90 V112 H90"/>
      <path d="M134 59 V78"/><path d="M122 98 V130 H134"/>
      <path d="M185 59 V70"/><path d="M172 90 V112 H185"/>
    </g>
    <g fill="#3fb7b3" stroke="#1e8a87" stroke-width="0.6">
      <rect x="22" y="45" width="36" height="14" rx="2"/>
      <rect x="72" y="45" width="36" height="14" rx="2"/>
      <rect x="116" y="45" width="36" height="14" rx="2"/>
      <rect x="167" y="45" width="36" height="14" rx="2"/>
    </g>
    <g fill="#fff" font-weight="700" text-anchor="middle">
      <text x="40" y="54">Lorem ipsum</text><text x="90" y="54">Lorem ipsum</text>
      <text x="134" y="54">Lorem ipsum</text><text x="185" y="54">Lorem ipsum</text>
    </g>
    <g fill="#3fb7b3" stroke="#1e8a87" stroke-width="0.6">
      <path d="M40 84 a13 3 0 0 1 26 0 v14 a13 3 0 0 1 -26 0z"/>
      <path d="M40 106 a13 3 0 0 1 26 0 v14 a13 3 0 0 1 -26 0z"/>
      <path d="M77 70 a13 3 0 0 1 26 0 v14 a13 3 0 0 1 -26 0z"/>
      <path d="M77 96 a13 3 0 0 1 26 0 v14 a13 3 0 0 1 -26 0z"/>
      <path d="M77 126 a13 3 0 0 1 26 0 v14 a13 3 0 0 1 -26 0z"/>
      <path d="M121 78 a13 3 0 0 1 26 0 v14 a13 3 0 0 1 -26 0z"/>
      <path d="M121 100 a13 3 0 0 1 26 0 v14 a13 3 0 0 1 -26 0z"/>
      <path d="M121 126 a13 3 0 0 1 26 0 v14 a13 3 0 0 1 -26 0z"/>
      <path d="M172 70 a13 3 0 0 1 26 0 v14 a13 3 0 0 1 -26 0z"/>
      <path d="M172 96 a13 3 0 0 1 26 0 v14 a13 3 0 0 1 -26 0z"/>
      <path d="M172 126 a13 3 0 0 1 26 0 v14 a13 3 0 0 1 -26 0z"/>
    </g>
    <g fill="none" stroke="#1e8a87" stroke-width="0.5">
      <path d="M40 84 a13 3 0 0 0 26 0"/><path d="M40 106 a13 3 0 0 0 26 0"/>
      <path d="M77 70 a13 3 0 0 0 26 0"/><path d="M77 96 a13 3 0 0 0 26 0"/><path d="M77 126 a13 3 0 0 0 26 0"/>
      <path d="M121 78 a13 3 0 0 0 26 0"/><path d="M121 100 a13 3 0 0 0 26 0"/><path d="M121 126 a13 3 0 0 0 26 0"/>
      <path d="M172 70 a13 3 0 0 0 26 0"/><path d="M172 96 a13 3 0 0 0 26 0"/><path d="M172 126 a13 3 0 0 0 26 0"/>
    </g>
    <g text-anchor="middle" font-weight="700">
      <text x="53" y="94">Lorem</text><text x="53" y="116">Lorem</text>
      <text x="90" y="80">Lorem</text><text x="90" y="106">Lorem</text><text x="90" y="136">Lorem</text>
      <text x="134" y="88">Lorem</text><text x="134" y="110">Lorem</text><text x="134" y="136">Lorem</text>
      <text x="185" y="80">Lorem</text><text x="185" y="106">Lorem</text><text x="185" y="136">Lorem</text>
    </g>
  </svg>
  <span class="footer-mark"></span>
  <footer class="slide-footer"><span>Private/Confidential</span><span>www.GlimmerlyOrbit.com</span></footer>
</section>

<!-- Content: bullets -->
<section class="slide" style="left:349px;top:437px">
  <h2 class="headline">LOREM IPSUM</h2>
  <ul class="bullets" style="position:absolute;left:20px;top:53px;font-size:5.4px">
    <li style="margin-bottom:9px">Lorem ipsum dolor sit amet, consectetuer adipiscing elit, sed diam non-</li>
    <li style="margin-bottom:9px">Lorem ipsum dolor sit amet, consectetuer adipiscing elit, sed diam non-</li>
    <li style="margin-bottom:9px">Lorem ipsum dolor sit amet, consectetuer adipiscing elit, sed diam non-</li>
    <li style="margin-bottom:9px">Lorem ipsum dolor sit amet, consectetuer adipiscing elit, sed diam non-</li>
    <li style="margin-bottom:9px">Lorem ipsum dolor sit amet, consectetuer adipiscing elit, sed diam non-</li>
    <li>Lorem ipsum dolor sit amet, consectetuer.</li>
  </ul>
  <span class="footer-mark"></span>
  <footer class="slide-footer"><span>Private/Confidential</span><span>www.GlimmerlyOrbit.com</span></footer>
</section>

<!-- Content: subtitles in two columns -->
<section class="slide" style="left:636px;top:437px">
  <h2 class="headline">LOREM IPSUM</h2>
  <div class="sub" style="position:absolute;left:10px;top:49px;width:118px">
    <p class="sub-title">Sub Title-1</p>
    <ul><li>Lorem ipsum dolor sit amet, etuer.</li><li>Adipiscing elit, sed diam non euismod</li></ul>
    <p class="sub-title">Sub Title-2</p>
    <ul><li>Lorem ipsum dolor sit amet, etuer.</li><li>Adipiscing elit, sed diam non isnod tinci-</li></ul>
    <p class="sub-title">Sub Title-3</p>
    <ul><li>Lorem ipsum dolor sit amet, etuer.</li><li>Edipiscing elit,onummy nibh euismod</li></ul>
  </div>
  <div class="sub" style="position:absolute;left:134px;top:49px;width:112px">
    <p class="sub-title">Sub Title-1</p>
    <ul><li>Lorem ipsum dolor sit amet, consectetuer.</li></ul>
    <p class="sub-title">Sub Title-2</p>
    <ul><li>Lorem ipsum dolor sit amet, consectetuer.</li><li>Adipiscing elit, sonummy nibh euismod</li></ul>
    <p class="sub-title">Sub Title-3</p>
    <ul><li>Lorem ipsum dolor sit amet, consectetuer.</li><li>Cdipiscing elit, s nonummy nibh euismod</li></ul>
  </div>
  <span class="footer-mark"></span>
  <footer class="slide-footer"><span>Private/Confidential</span><span>www.GlimmerlyOrbit.com</span></footer>
</section>

<!-- Closing slide -->
<section class="slide" style="left:923px;top:437px">
  <div class="lockup" style="top:46px">
    <div class="lockup-brand"><div class="lockup-name"><span class="lockup-dot"></span>Glimmerly Orbit</div><div class="lockup-tagline">Every Hour Shines Bright</div></div>
    <span class="lockup-divider"></span>
    <div class="lockup-partner"><span class="partner-dot"></span>Coalition of Harbor Artisans</div>
  </div>
  <p style="position:absolute;top:90px;width:100%;text-align:center;font-family:'Open Sans',Arial,sans-serif;font-weight:800;font-size:16px;color:var(--purple)">Thank You!</p>
  <p style="position:absolute;top:110px;width:100%;text-align:center;font-weight:700;font-size:9px;color:var(--teal)">For your attention</p>
  <footer class="slide-footer"><span>Private/Confidential</span><span>www.GlimmerlyOrbit.com</span></footer>
</section>

</body>
</html>
```